Business Card Design for a Sound engineer and DJ

We would like a residn of the business card.

Logo must remain the same.
The card is for the owner of the company.
The business card is in Arabic as the company is based in Kuwait.
The company specializes in sound engineering for singers concerts and events and in addition DJ.
The color options is up to the designer but we would like it masculine as the owner is a man.

Target Market(s)

All ages

Industry/Entity Type

Media

Contact Information for Business Card

Name:
Eng. Tarek Halabi
م/طارق حلبي

The name above is in Arabic and English.

Title: General Manager
Mobile: +965 66307852
Office: +965 22486037
Email: info@sawtarin.net

Address:
Office no. 3
1st floor
Almarfa Complex
Rashed AlQeblawi St.
Salmiya
Kuwait

Instagram: @sawtarin
Snap: sawtarin

Requirements
Nice to have
• can we have Instagram icon and snap icon and a phone vector and email?
• Instead of writing the words

```html
<!DOCTYPE html>
<html lang="en">
<head>
<meta charset="utf-8">
<title>Sawtarin Business Card</title>
<link href="https://fonts.googleapis.com/css2?family=Open+Sans:wght@400;600&family=Cairo:wght@400;600&display=swap" rel="stylesheet">
<style>
  :root {
    --stage: #ecebef;
    --card: #ffffff;
    --violet: #7b3f9e;
    --violet-deep: #6a3a94;
    --violet-soft: #b79ad0;
    --blue-violet: #5a5fb8;
    --magenta: #b0408f;
    --text-muted: #7c4a9c;
  }
  * { box-sizing: border-box; margin: 0; padding: 0; }
  html, body { width: 1200px; height: 858px; overflow: hidden; }
  body {
    background: var(--stage);
    font-family: "Open Sans", sans-serif;
    display: flex;
    align-items: center;
    justify-content: center;
    gap: 40px;
  }
  .card {
    width: 540px;
    height: 310px;
    background: var(--card);
    position: relative;
    box-shadow: 0 6px 18px rgba(60, 40, 80, 0.18);
    overflow: hidden;
  }

  /* brand-side card */
  .card--brand {
    background: linear-gradient(180deg, #ffffff 0%, #ffffff 45%, #c9b2dc 70%, #8f5fae 100%);
    display: flex;
    align-items: center;
    justify-content: center;
  }
  .brand {
    display: flex;
    align-items: center;
    gap: 14px;
  }
  .brand__mark {
    width: 18px; height: 18px;
    background: var(--violet);
    border-radius: 50%;
  }
  .brand__text { display: flex; flex-direction: column; }
  .brand__name {
    font-size: 40px;
    font-weight: 600;
    color: var(--violet);
    letter-spacing: 6px;
    line-height: 1;
  }
  .brand__tagline {
    font-size: 11px;
    letter-spacing: 2.6px;
    color: var(--violet);
    margin-top: 8px;
  }
  .brand__tagline-ar {
    font-family: "Cairo", sans-serif;
    font-size: 13px;
    color: var(--violet);
    direction: rtl;
    text-align: right;
    line-height: 1.5;
  }

  /* contact-side card */
  .card--contact { padding: 28px 30px; }
  .person__name {
    font-size: 19px;
    color: var(--blue-violet);
    line-height: 1.2;
  }
  .person__name-ar {
    font-family: "Cairo", sans-serif;
    font-size: 17px;
    color: var(--blue-violet);
    direction: rtl;
    text-align: left;
    unicode-bidi: plaintext;
    line-height: 1.3;
  }
  .person__title {
    font-size: 12px;
    color: var(--violet-deep);
    margin-top: 2px;
  }
  .contact-list { list-style: none; margin-top: 16px; }
  .contact-list li {
    display: flex; align-items: center; gap: 8px;
    font-size: 12.5px; color: var(--violet-deep);
    line-height: 1.55;
  }
  .contact-list--social { margin-top: 12px; }
  .icon { width: 12px; height: 12px; flex: none; }
  .social-dot {
    width: 11px; height: 11px; flex: none;
    background: var(--violet); border-radius: 2px;
  }
  .social-dot--round { border-radius: 50%; }

  .card__brand-small {
    position: absolute;
    right: 30px; top: 150px;
    text-align: right;
  }
  .card__brand-small .brand__name { font-size: 24px; letter-spacing: 4px; }
  .card__brand-small .brand__tagline { font-size: 8px; letter-spacing: 1.6px; margin-top: 4px; }
  .card__brand-small .brand__tagline-ar { font-size: 10px; }

  .address {
    position: absolute;
    right: 30px; bottom: 24px;
    font-size: 12.5px;
    color: var(--violet-deep);
    text-align: left;
    line-height: 1.5;
  }
</style>
</head>
<body>

  <section class="card card--brand" aria-label="Card front">
    <div class="brand">
      <span class="brand__mark"></span>
      <div class="brand__text">
        <span class="brand__name">SAWTARIN</span>
        <span class="brand__tagline">DJ - SOUND ENG. - LIGHTING</span>
        <span class="brand__tagline-ar">دي جي - هندسة صوت - إضاءة</span>
      </div>
    </div>
  </section>

  <section class="card card--contact" aria-label="Card back">
    <p class="person__name">Eng. Tarek Halabi</p>
    <p class="person__name-ar" dir="rtl">م/طارق حلبي</p>
    <p class="person__title">General Manager</p>

    <ul class="contact-list">
      <li>
        <svg class="icon" viewBox="0 0 12 12"><rect x="3" y="0.5" width="6" height="11" rx="1.2" fill="none" stroke="var(--violet)" stroke-width="1.2"/><circle cx="6" cy="9.6" r="0.7" fill="var(--violet)"/></svg>
        +965 66307852
      </li>
      <li>
        <svg class="icon" viewBox="0 0 12 12"><path d="M1 4 Q6 0 11 4 L10 5.5 L8 4.6 L8 3.6 Q6 3 4 3.6 L4 4.6 L2 5.5 Z" fill="var(--violet)"/><rect x="2.5" y="6" width="7" height="5" rx="1" fill="var(--violet)"/></svg>
        +965 22486037
      </li>
      <li>
        <svg class="icon" viewBox="0 0 12 12"><rect x="0.5" y="2" width="11" height="8" fill="var(--violet)"/><path d="M0.8 2.4 L6 6.8 L11.2 2.4" fill="none" stroke="#fff" stroke-width="1"/></svg>
        info@sawtarin.net
      </li>
    </ul>

    <ul class="contact-list contact-list--social">
      <li><span class="social-dot"></span>@sawtarin</li>
      <li><span class="social-dot social-dot--round"></span>sawtarin</li>
    </ul>

    <div class="card__brand-small">
      <div class="brand__name">SAWTARIN</div>
      <div class="brand__tagline">DJ - SOUND ENG. - LIGHTING</div>
      <div class="brand__tagline-ar">دي جي - هندسة صوت - إضاءة</div>
    </div>

    <address class="address" style="font-style: normal;">
      Office no. 3, 1st floor, Almarfa Complex<br>
      Rashed AlQeblawi St., Salmiya, Kuwait
    </address>
  </section>

</body>
</html>
```